Rollup Banner & Flyer für eine Messe "Erfolg durch Innovation"

Wir benötigten für eine Messe einen Roll Up Banner und Flyer zum verteilen. Gerne basierend auf der aktuellen Firmenpräsentation und mit unseren Referenzen.
Im flyer sollen unserer Leistungen (Datenanalyse, Simulation, Optimierung und Webapplikation) dargestellt werden mit einem kleinen Text und einem aussagekräftigen bild. (https://www.kalvento.ch/leistungen/)

Target Market(s)

Industrie

Industry/Entity Type

Simulation

Font styles to use
Sans Serif
Other font styles liked:
• Roboto

Requirements
Must have
• Logo, Referenzen

```html
<!DOCTYPE html>
<html lang="de">
<head>
<meta charset="utf-8">
<title>Kalvento – Flyer</title>
<link rel="stylesheet" href="https://fonts.googleapis.com/css2?family=Roboto:wght@400;500;700;900&display=swap">
<style>
  :root {
    --backdrop: #e5e5e5;
    --paper: #ffffff;
    --accent: #dcdb66;
    --accent-soft: #f4f3d2;
    --ink: #111111;
    --light: #ffffff;
  }
  * { margin: 0; padding: 0; box-sizing: border-box; }
  html, body {
    width: 923px; height: 1200px; overflow: hidden;
    background: var(--backdrop);
    font-family: "Roboto", Arial, sans-serif;
    color: var(--ink);
  }
  .flyer {
    position: absolute; left: 263px; top: 105px;
    width: 396px; height: 989px;
    background: var(--paper); overflow: hidden;
  }
  .flyer-shapes { position: absolute; inset: 0; width: 396px; height: 989px; }
  .abs { position: absolute; }

  .brand {
    left: 20px; top: 19px; display: flex; align-items: center; gap: 6px;
    color: var(--light); font-weight: 700; font-size: 16px; letter-spacing: .3px;
  }
  .brand-dot { width: 16px; height: 16px; border-radius: 50%; background: var(--light); }

  .headline {
    left: 47px; top: 56px; width: 320px;
    color: var(--light); font-weight: 700; font-size: 22px; line-height: 26px;
  }
  .subline {
    left: 47px; top: 115px; width: 272px;
    color: var(--light); font-size: 14px; line-height: 17px;
  }
  .contact {
    right: 17px; top: 230px; text-align: right;
    font-size: 12.5px; line-height: 16px; font-style: normal;
  }
  .contact p + p { margin-top: 16px; }

  .service-title { font-weight: 700; font-size: 22px; line-height: 26px; }
  .service-text { font-size: 10px; line-height: 13.8px; }

  .icon-slot { background: var(--accent-soft); border-radius: 12px; }

  .t-data { left: 29px; top: 322px; }
  .p-data { left: 31px; top: 356px; width: 200px; }
  .i-data { left: 254px; top: 340px; width: 99px; height: 98px; }

  .t-sim { left: 146px; top: 467px; }
  .p-sim { left: 147px; top: 497px; width: 210px; }
  .i-sim { left: 26px; top: 468px; width: 106px; height: 88px; }

  .t-opt { left: 33px; top: 598px; }
  .p-opt { left: 34px; top: 632px; width: 208px; }
  .i-opt { left: 257px; top: 620px; width: 109px; height: 107px; }

  .t-web { left: 168px; top: 748px; }
  .p-web { left: 148px; top: 780px; width: 222px; }
  .i-web { left: 24px; top: 764px; width: 108px; height: 105px; }
</style>
</head>
<body>
<main class="flyer">
  <svg class="flyer-shapes" viewBox="0 0 396 989" aria-hidden="false">
    <defs>
      <linearGradient id="heroTone" x1="0" y1="0" x2="1" y2="1">
        <stop offset="0" stop-color="#0a1524"/>
        <stop offset=".6" stop-color="#1d2e45"/>
        <stop offset="1" stop-color="#2c2f44"/>
      </linearGradient>
    </defs>
    <polygon role="img" aria-label="Foto: digitale Dashboards mit Diagrammen und Kennzahlen auf dunklem Hintergrund"
             points="0,0 396,0 396,190 0,296" fill="url(#heroTone)"/>
    <polygon class="hero-band" points="0,296 396,190 396,204 0,310" fill="var(--accent)"/>

    <g stroke="var(--accent)" stroke-width="2">
      <line x1="30" y1="454" x2="367" y2="454"/>
      <line x1="30" y1="589" x2="367" y2="589"/>
      <line x1="30" y1="744" x2="367" y2="744"/>
    </g>

    <polygon class="footer-band" points="0,948 396,896 396,910 0,962" fill="var(--accent)"/>
    <polygon class="footer-block" points="0,972 396,920 396,989 0,989" fill="var(--ink)"/>
  </svg>

  <div class="abs brand"><span class="brand-dot"></span>Kalvento</div>

  <h1 class="abs headline">Ihr nächster Schritt –<br>intelligenter gemacht.</h1>
  <p class="abs subline">Strategische Entscheidungen – unterstützt durch Simulation, optimiert durch Analytik.</p>

  <address class="abs contact">
    <p>Seestrasse 14<br>7310 Bad Ragaz</p>
    <p>+41 81 734 26 90<br>info@kalvento.ch</p>
  </address>

  <h2 class="abs service-title t-data">Datenanalyse</h2>
  <p class="abs service-text p-data">Datenanalyse macht Prozesse sichtbar, erkennt Muster und schafft eine objektive Grundlage für Entscheidungen. Wir strukturieren, bereinigen und analysieren Daten so, dass sie einen echten Nutzen erzeugen.</p>
  <div class="abs icon-slot i-data" role="img" aria-label="Symbol: Datenbank mit umlaufenden Pfeilen"></div>

  <h2 class="abs service-title t-sim">Simulation</h2>
  <p class="abs service-text p-sim">Simulation bildet reale Prozesse digital ab, damit Abläufe, Kapazitäten und Varianten risikofrei getestet werden können.</p>
  <div class="abs icon-slot i-sim" role="img" aria-label="Symbol: Monitor mit Dashboard"></div>

  <h2 class="abs service-title t-opt">Optimierung</h2>
  <p class="abs service-text p-opt">Optimierung sucht automatisch nach der besten Lösung – sei es bei Planung, Ressourcen, Routen oder Abläufen. Mit Algorithmen und intelligenten Modellen finden wir Varianten, die Kosten senken, Kapazitäten besser nutzen und Entscheidungen beschleunigen.</p>
  <div class="abs icon-slot i-opt" role="img" aria-label="Symbol: Dokument mit Zahnrad und verzweigten Abläufen"></div>

  <h2 class="abs service-title t-web">Webapplikationen</h2>
  <p class="abs service-text p-web">Wir entwickeln individuelle Webapplikationen, die Daten, Simulationen und Optimierungen in einem benutzerfreundlichen Tool zusammenführen. So entstehen Lösungen, die direkt im Alltag genutzt werden – einfach, schnell und ohne Installation.</p>
  <div class="abs icon-slot i-web" role="img" aria-label="Symbol: Bildschirm mit Browserfenster und Mauszeiger"></div>
</main>
</body>
</html>
```